Gold Award for Hygiene Excellence

We are providing food safety consultancy to restaurant business in the uk. We would like to prepare an award sticker for business that work with us to get sticker award if they got 5 star hygiene rating consecutively in the their last 3 inspections. Normally, they display hygiene scores that are green color on their shop's window. So it should be catchy color for people easily detect the award. Size A5

```html
<!DOCTYPE html>
<html lang="en">
<head>
<meta charset="utf-8">
<title>Gold Award for Hygiene Excellence</title>
<link href="https://fonts.googleapis.com/css2?family=Cinzel:wght@500&family=Montserrat:wght@500;600;700&display=swap" rel="stylesheet">
<style>
  :root {
    --page: #ffffff;
    --forest: #1f261c;
    --paper: #ffffff;
    --gold-light: #f3dc8e;
    --gold-mid: #c9a24a;
    --gold-dark: #8a6a25;
    --lime: #b7cc1c;
    --grey: #8a8a8a;
    --brand: #7d8a3a;
  }
  * { margin: 0; padding: 0; box-sizing: border-box; }
  html, body {
    width: 800px; height: 1200px; overflow: hidden;
    background: var(--page);
  }
  .award-card {
    position: absolute;
    left: 40px; top: 346px;
    width: 720px; height: 508px;
    background: var(--paper);
    box-shadow: 2px 6px 10px rgba(0,0,0,0.35);
    font-family: "Montserrat", sans-serif;
  }
  .award-card__panel {
    position: absolute; left: 0; top: 0;
    width: 720px; height: 403px;
    background: var(--forest);
  }
  .brand-tab {
    position: absolute; left: 265px; top: 0;
    width: 190px; height: 69px;
    background: var(--paper);
    display: flex; flex-direction: column; align-items: center; justify-content: center;
    color: var(--brand);
    font-family: "Montserrat", sans-serif;
    font-weight: 500;
    line-height: 1.1;
  }
  .brand-tab__name { font-size: 18px; letter-spacing: 4px; }
  .brand-tab__tagline { font-size: 8px; letter-spacing: 0.5px; }
  .award-title {
    position: absolute; left: 0; top: 110px; width: 720px;
    text-align: center;
    font-family: "Cinzel", serif;
    font-weight: 500;
    font-size: 84px;
    line-height: 1;
    letter-spacing: 1px;
    background: linear-gradient(180deg, var(--gold-light) 0%, var(--gold-mid) 50%, var(--gold-dark) 100%);
    -webkit-background-clip: text; background-clip: text;
    color: transparent;
    filter: drop-shadow(3px 4px 3px rgba(0,0,0,0.6));
  }
  .cutlery-badge {
    position: absolute; left: 318px; top: 235px;
    width: 82px; height: 82px;
  }
  .award-tagline {
    position: absolute; left: 0; top: 345px; width: 720px;
    display: flex; align-items: center; justify-content: center; gap: 12px;
    color: #ffffff;
    font-size: 17px; font-weight: 500; letter-spacing: 0.3px;
  }
  .award-tagline__rule { width: 40px; height: 2px; background: #ffffff; border-radius: 1px; }
  .score-row {
    position: absolute; left: 0; top: 425px; width: 720px;
    display: flex; justify-content: center; gap: 24px;
  }
  .score-badge {
    width: 30px; height: 30px; border-radius: 50%;
    border: 3px solid var(--lime);
    display: flex; align-items: center; justify-content: center;
    color: var(--grey); font-size: 16px; font-weight: 600;
  }
  .score-caption {
    position: absolute; left: 0; top: 473px; width: 720px;
    text-align: center;
    color: var(--grey); font-size: 13px; font-weight: 700;
  }
  .validity {
    position: absolute; right: 24px; top: 488px;
    color: var(--grey); font-size: 8.5px; font-weight: 700;
  }
</style>
</head>
<body>
  <div class="award-card">
    <div class="award-card__panel">
      <div class="brand-tab">
        <span class="brand-tab__name">CORVANE</span>
        <span class="brand-tab__tagline">Food Safety Advisory</span>
      </div>
      <h1 class="award-title">GOLD AWARD</h1>
      <svg class="cutlery-badge" viewBox="0 0 82 82" aria-hidden="true">
        <defs>
          <linearGradient id="goldFill" x1="0" y1="0" x2="0" y2="1">
            <stop offset="0" stop-color="#f3dc8e"/>
            <stop offset="0.5" stop-color="#c9a24a"/>
            <stop offset="1" stop-color="#8a6a25"/>
          </linearGradient>
        </defs>
        <circle cx="41" cy="41" r="38" fill="none" stroke="url(#goldFill)" stroke-width="3"/>
        <path d="M30 20 v12 M33.5 20 v12 M37 20 v12 M30 32 q3.5 5 7 0" fill="none" stroke="url(#goldFill)" stroke-width="2"/>
        <rect x="32" y="34" width="3" height="30" rx="1.5" fill="url(#goldFill)"/>
        <path d="M47 20 q8 6 5 24 h-3 v20 h-3 V21 z" fill="url(#goldFill)"/>
      </svg>
      <div class="award-tagline">
        <span class="award-tagline__rule"></span>
        <span>FOR HYGIENE EXCELLENCE</span>
        <span class="award-tagline__rule"></span>
      </div>
    </div>
    <div class="score-row">
      <span class="score-badge">5</span>
      <span class="score-badge">5</span>
      <span class="score-badge">5</span>
    </div>
    <p class="score-caption">THREE CONSECUTIVE TOP SCORES</p>
    <p class="validity">VALID UNTIL: JUNE 2024</p>
  </div>
</body>
</html>
```